Web Design Project

I'm looking for a major redesign for my existing photographic art website: www.brightmeadowframes.com. Here are my complaints about the current layout: 1) It looks unsophisticated (we will, of course, delete the "sale" banner; 2) the images are vastly too small when displayed in the gallery; 3) I'm not wild about the navigation; 4) the Flash has got to go; 4) there has to be an easy way to significantly enlarge the photos for viewing; 5) the copy is a bit over the top - we will be rewriting it. Other than that, it's a good site :)

The market for the photography is principally commercial applications - interior designers, etc. who are concerned with how these images will look in hospitals, office buildings, etc. The leading competitor in this space has a much better site: www.walterpikens.com. Another site worth viewing is: www.morvelt.com. This site is much more akin to my site.

We will be reducing the number of photos available. Total count will be approximately 400. The largest collection will be the "digital garden" - close up photography of flowers, plants, etc.
Updates

I am amazed at the quality of the submissions - which has made the selection process very, very difficult. Each of you should be very proud of the quality of work you produce. Beyond this web-site, which is a "sideline" for me, I run a large marketing organization....and have shared these submissions with all of my colleagues who were duly impressed. Hopefully we will have an opportunity to work with you on a differentp project!

Thank you!!!
Peter

Industry/Entity Type

Digital

```html
<!DOCTYPE html>
<html lang="en">
<head>
<meta charset="utf-8">
<title>Bright Meadow Frames</title>
<link href="https://fonts.googleapis.com/css2?family=Cinzel:wght@400;500&family=Poiret+One&family=Ubuntu:wght@400;500;700&display=swap" rel="stylesheet">
<style>
:root{
  --page:#0c0a0a;
  --panel:#000;
  --gold:#e8c874;
  --gold-soft:#f0d9a0;
  --text-gold:#f2c95c;
  --rule:#6b5a36;
  --sale-red:#c8281a;
  --orange:#ff7f15;
  --orange-text:#ff8a1f;
  --brick:#c0240e;
  --cream:#f3c97a;
  --footer:#6a6460;
  --social:#8a7446;
}
*{margin:0;padding:0;box-sizing:border-box}
html,body{width:1200px;height:1200px;overflow:hidden;background:var(--page);font-family:"Ubuntu",sans-serif}
.canvas{position:relative;width:1200px;height:1200px}
.panel{position:absolute;left:88px;top:100px;width:1024px;height:955px;background:var(--panel)}
.abs{position:absolute}
.brand{left:0;width:1200px;top:136px;text-align:center;font-family:"Cinzel",serif;font-weight:400;font-size:30px;color:var(--gold);letter-spacing:1.5px;line-height:1}
.cart{left:900px;top:120px;width:172px;text-align:right;font-size:11px;color:var(--gold);letter-spacing:.3px}
.cart svg{display:block;margin:0 70px 4px auto}
.rule{left:124px;width:952px;height:1px;background:var(--rule)}
.nav-mark{left:166px;top:209px;width:40px;height:12px;background:var(--gold);opacity:.7;border-radius:6px}
.nav{left:150px;top:228px;width:900px;display:flex;justify-content:space-between;font-family:"Cinzel",serif;font-size:15.5px;color:var(--gold);letter-spacing:.3px;list-style:none}
.sale{left:138px;top:297px;font-family:"Cinzel",serif;font-weight:400;font-size:24.5px;color:var(--sale-red);letter-spacing:.8px}
.sale .pct{color:var(--orange)}
.sale-note{left:140px;top:331px;width:524px;text-align:center;font-size:12px;line-height:14px;color:var(--gold-soft)}
.search-label{left:140px;top:372px;font-family:"Poiret One",sans-serif;font-size:20px;color:var(--orange-text)}
.search-label small{font-size:15px;margin-left:4px}
.search-box{left:144px;top:408px;width:257px;height:37px;border:1px solid var(--gold)}
.search-btn{left:400px;top:408px;width:35px;height:37px;background:#e6c46c}
.bio{left:141px;width:388px;font-size:12.2px;line-height:14.5px;color:var(--text-gold);letter-spacing:.5px}
.tagline{left:140px;top:727px;font-family:"Poiret One",sans-serif;font-size:20px;color:var(--orange-text);letter-spacing:.6px}
.frame{left:662px;top:291px;width:358px;height:499px;background:linear-gradient(135deg,#f4d777,#a57a1d 30%,#e8c258 55%,#8d6512 80%,#e6c45e);padding:22px 24px}
.mat{width:100%;height:100%;background:#fffdf6;padding:10px}
.photo{width:100%;height:100%;background:radial-gradient(ellipse at 60% 40%,#e8401c 0%,#c83012 35%,transparent 60%),linear-gradient(160deg,#b8391f,#2f8f9e 50%,#c24018 85%)}
.arrow{top:621px}
.subscribe{left:140px;top:812px;width:415px;height:158px;background:var(--orange);padding:22px 16px;color:#000}
.subscribe h3{font-weight:400;font-size:25px;display:inline}
.subscribe h3 small{font-size:12px;margin-left:4px;font-weight:500}
.subscribe p{font-size:12px;line-height:14.5px;margin-top:12px;letter-spacing:.3px;font-weight:500}
.email{position:absolute;left:16px;top:118px;width:170px;height:24px;background:#fff;font-size:11px;padding:6px 9px}
.login{position:absolute;left:193px;top:126px;font-weight:700;font-size:13px;color:#fff;letter-spacing:.5px}
.contact{left:557px;top:812px;width:517px;height:158px;background:var(--brick);padding:18px 14px}
.contact h3{font-family:"Cinzel",serif;font-weight:400;font-size:25px;color:var(--cream);letter-spacing:2.4px;white-space:nowrap}
.contact dl{margin-top:14px;font-weight:500;font-size:18px;line-height:23px;display:flex;letter-spacing:.4px}
.contact dt{color:#000;width:114px}
.contact dd{color:#ffa23a}
.social{right:129px;top:983px;display:flex;align-items:center;gap:3px;font-family:"Poiret One",sans-serif;font-size:13px;color:var(--orange-text)}
.social span{margin-right:3px}
.social i{display:block;width:24px;height:24px;border-radius:2px;background:var(--social)}
.footer-nav{left:88px;top:1075px;font-size:11px;color:var(--footer);letter-spacing:.3px}
.copy{left:88px;top:1101px;font-size:11px;color:var(--footer)}
</style>
</head>
<body>
<div class="canvas">
  <div class="panel"></div>

  <header>
    <div class="abs brand">Bright Meadow Frames</div>
    <div class="abs cart">
      <svg width="24" height="20" viewBox="0 0 24 20" fill="none" stroke="#ff7f15" stroke-width="1.6"><path d="M1 2h4l3 11h12l2-8H7"/><circle cx="10" cy="17" r="1.6"/><circle cx="18" cy="17" r="1.6"/></svg>
      your shopping cart is empty
    </div>
    <div class="abs rule" style="top:197px"></div>
    <div class="abs nav-mark" role="img" aria-label="Small ornament marking the active menu item"></div>
    <ul class="abs nav"><li>GALLERY</li><li>ARCHITECTS/DESIGNERS</li><li>ABOUT THE ARTIST</li><li>ORDERING INFORMATION</li><li>CONTACT US</li></ul>
    <div class="abs rule" style="top:262px"></div>
  </header>

  <main>
    <h2 class="abs sale">SALE! ALL PHOTOGRAPHS <span class="pct">30% OFF.</span></h2>
    <p class="abs sale-note">Discount will be applied automatically in the shopping cart<br>as part of the ordering process.</p>
    <div class="abs search-label">Search <small>for your picture from the collections</small></div>
    <div class="abs search-box"></div>
    <div class="abs search-btn"><svg width="35" height="37" viewBox="0 0 35 37" fill="none" stroke="#fff" stroke-width="2.4"><circle cx="15" cy="16" r="7"/><path d="M20 21l8 8" stroke-linecap="round" stroke-width="3.5"/></svg></div>

    <p class="abs bio" style="top:475px">During his days with the Monarchs, Peter also served as a freelance photojournalist for local newspapers and magazines, including The Riverton Star and Riverton Magazine. But as the years moved on, so did Peter’s interests.</p>
    <p class="abs bio" style="top:561px">During his days with the Monarchs, Peter also served as a freelance photojournalist for local newspapers and magazines, including The Riverton Star and Riverton Magazine. But as the years moved on, so did Peter’s interests.</p>
    <p class="abs bio" style="top:648px">During his days with the Monarchs, Peter also served as a freelance photojournalist for local newspapers and magazines, including The Riverton Star and Riverton Magazine. But as the years moved on, so did Peter’s interests.</p>
    <p class="abs tagline">photography that transcends our normal view of the world</p>

    <svg class="abs arrow" style="left:614px" width="30" height="30" viewBox="0 0 30 30" fill="none" stroke="#e8c874" stroke-width="2"><circle cx="15" cy="15" r="13"/><path d="M18 8l-8 7 8 7z" fill="#e8c874"/></svg>
    <div class="abs frame"><div class="mat"><div class="photo" role="img" aria-label="Close-up photograph of red leaves on a green stem against a blurred teal background"></div></div></div>
    <svg class="abs arrow" style="left:1034px" width="30" height="30" viewBox="0 0 30 30" fill="none" stroke="#e8c874" stroke-width="2"><circle cx="15" cy="15" r="13"/><path d="M12 8l8 7-8 7z" fill="#e8c874"/></svg>

    <section class="abs subscribe">
      <h3>Subscribe<small>join our mailing list</small></h3>
      <p>Would you like to be kept informed about beautiful landscape photography, new workshops and courses<br>as well as receive exclusive exhibition preview invites?</p>
      <div class="email">email</div>
      <div class="login">LOGIN</div>
    </section>
    <section class="abs contact">
      <h3>SALE! ALL PHOTOGRAPHS 30% OFF.</h3>
      <dl><dt>Contact us :</dt><dd>877-555-0142<br>peterhalvern@brightmeadowframes.com</dd></dl>
    </section>

    <div class="abs social"><span>discover peter halvern</span><i role="img" aria-label="Social link"></i><i role="img" aria-label="Social link"></i><i role="img" aria-label="Social link"></i><i role="img" aria-label="Social link"></i></div>
  </main>

  <footer>
    <p class="abs footer-nav">Gallery &nbsp;|&nbsp; Architects/Designers &nbsp;|&nbsp; About the Artist &nbsp;|&nbsp; Ordering Information &nbsp;|&nbsp; Contact Us</p>
    <p class="abs copy">© 2012 Halvern Photography</p>
  </footer>
</div>
</body>
</html>
```